The Festival! Poster for an Annual Dance Showcase

We are looking for a dynamic festival/concert style poster for our annual dance showcase featuring at least one image of our dancers and the main information. The main image should be one of the dancers but there can be a collage of the dancers or smaller images around the poster. I have included some reference images but it can vary from them.

Must have this information;
Date - May 22-26
Location - Mabel Corwin Hale Theatre
Tickets - Vondo.bm

Target Market(s)

Parents and people who love dance

Industry/Entity Type

Dance

Font styles to use
Sans Serif

Colors
E54698
E96AAD
F1A4CE
F9D9EA
FCEFF6

Requirements
Must have
• Logo, Date and Location, Picture of Dancer

```html
<!DOCTYPE html>
<html lang="en">
<head>
<meta charset="utf-8">
<title>Annual Dance Showcase Poster</title>
<link rel="stylesheet" href="https://fonts.googleapis.com/css2?family=Montserrat:wght@600;700&family=Oswald:wght@500&display=swap">
<style>
  :root {
    --stage-bg: #c4c4c4;
    --poster-top: #fbe1ee;
    --poster-mid: #fcedf5;
    --poster-bottom: #ffffff;
    --magenta: #e6079b;
    --plum: #8c1d63;
    --ink: #111111;
    --photo-skin: #d9b79a;
    --photo-gold: #f2c21a;
    --photo-coral: #ee7a66;
    --photo-black: #2a2226;
  }
  * { margin: 0; padding: 0; box-sizing: border-box; }
  html, body { width: 1200px; height: 839px; overflow: hidden; }
  body {
    background: var(--stage-bg);
    position: relative;
    font-family: "Montserrat", Arial, sans-serif;
  }
  .poster {
    position: absolute;
    left: 341px;
    top: 20px;
    width: 518px;
    height: 800px;
    background: linear-gradient(180deg, var(--poster-top) 0%, var(--poster-mid) 55%, var(--poster-bottom) 100%);
    overflow: hidden;
  }
  .brand {
    position: absolute;
    top: 38px;
    left: 0;
    width: 100%;
    display: flex;
    justify-content: center;
    align-items: center;
    gap: 10px;
  }
  .brand-dot {
    width: 30px;
    height: 30px;
    border-radius: 50%;
    background: var(--magenta);
  }
  .brand-name {
    color: var(--magenta);
    font-weight: 700;
    font-size: 17px;
    line-height: 1.15;
    letter-spacing: 0.3px;
    text-transform: uppercase;
  }
  .dancers-photo {
    position: absolute;
    left: 58px;
    top: 132px;
    width: 398px;
    height: 348px;
    border-radius: 6px;
    background:
      radial-gradient(ellipse 30% 55% at 24% 55%, var(--photo-skin) 0%, rgba(217,183,154,0) 100%),
      radial-gradient(ellipse 25% 40% at 52% 62%, var(--photo-gold) 0%, rgba(242,194,26,0) 100%),
      radial-gradient(ellipse 22% 30% at 55% 38%, var(--photo-black) 0%, rgba(42,34,38,0) 100%),
      radial-gradient(ellipse 28% 55% at 80% 50%, var(--photo-coral) 0%, rgba(238,122,102,0) 100%),
      linear-gradient(180deg, #f7d6e7 0%, #f4c9de 100%);
  }
  .headline {
    position: absolute;
    top: 514px;
    left: 0;
    width: 100%;
    text-align: center;
    font-family: "Oswald", "Arial Narrow", sans-serif;
    font-weight: 500;
    text-transform: uppercase;
    line-height: 1;
  }
  .headline-line1 { display: block; color: var(--magenta); font-size: 78px; letter-spacing: 0.5px; }
  .headline-line2 { display: block; color: var(--plum); font-size: 78px; margin-top: -8px; letter-spacing: 0.5px; }
  .venue {
    position: absolute;
    top: 676px;
    width: 100%;
    text-align: center;
    font-size: 10.5px;
    font-weight: 700;
    color: var(--ink);
    text-transform: uppercase;
    letter-spacing: 0.3px;
  }
  .date {
    position: absolute;
    top: 690px;
    width: 100%;
    text-align: center;
    font-family: "Oswald", "Arial Narrow", sans-serif;
    font-weight: 500;
    font-size: 48px;
    color: var(--ink);
    line-height: 1.1;
  }
  .tickets {
    position: absolute;
    top: 755px;
    width: 100%;
    text-align: center;
    font-size: 10.5px;
    font-weight: 700;
    color: var(--ink);
    text-transform: uppercase;
    letter-spacing: 0.3px;
  }
</style>
</head>
<body>
  <main class="poster">
    <header class="brand">
      <span class="brand-dot"></span>
      <span class="brand-name">Leaping Arc<br>School of Dance</span>
    </header>
    <div class="dancers-photo" role="img" aria-label="Photograph of three dancers in flowing nude, yellow-and-black and coral costumes posed mid-movement"></div>
    <h1 class="headline">
      <span class="headline-line1">Annual Dance</span>
      <span class="headline-line2">Showcase</span>
    </h1>
    <p class="venue">Mabel Corwin Hale Theatre</p>
    <p class="date">MAY - 22/26 - 2025</p>
    <p class="tickets">Tickets - Vondo.bm</p>
  </main>
</body>
</html>
```